2 Page Simple Modern Flyer for Upholstery Company!

I need a 2 sided printed flyer designed to showcase our company, Tarnwick Upholstery. We specialize in custom Upholstery work on booths, banquettes, chairs, etc for restaurants, bars, cafes, medical clinics, schools, condo towers, etc. I need the flyer to combine a brief description and history of the company, the logo, address & contact info as well as several provided project photos with a title of that job and company. Finally I need to have a some sort of list to show the different clients we have worked with.
Those clients include:
Halvern Arena
The Silver Quarry Casino
Dunmo
Corvello Pizza
PKLU
Juniper Hall
Faithful Teds
Oar & Lantern
Brackley Crossing Mall
Kesterfield Polytechnic
Torvane
And Many more.
This is the brief description of the company needed:
Tarnwick Upholstery has been serving North America for over 60 years. The company began as a family owned and operated business and has grown into a complete manufacturing facility. We can carry your vision straight through the manufacturing process, from initial drawings to finished product, including foam, fabric, framework, and associated millwork. Our 25,000 square foot facility has computer controlled cutters for both fabric and wood cutting capabilities. We have the capacity to take an original design and create products to meet your specifications, or adapt our standardized designs to fit your vision. We have a library of standard configurations that are customizable to meet almost any requirements.
The Contact info that needs to be included:
555-318-6472
www.tarnwickupholstery.example
4182 Mossvale Rd. Edmonton, AB. T9X 7K1
I will include the logo image and the several other photos that I would like to be used. One of the photos (The Silver Quarry Casino) I would like used in a bigger capacity.
I would like the look to be clean, simple and modern, but also incorporate some depth of a perhaps a few different shades of blues, greys, blacks and whites, similar to the logo design. I will attach a few photo examples of design I liked.
Let me know immediately if you have any questions or need any references.
Thanks.
Target Market(s)
Designers, Architects, Builders, Contractors, Business Owners.
Industry/Entity Type
It Company
Font styles to use
Requirements
Must have
- A simple modern design. Possibly using different geometric shapes (traingles, diamonds, squares, rectangles, etc) similar to the examples provided.
- Different Shades of blue, grey and black as the color themes.
- -The provided company description
- -The provided contact info
- -The logo provided
Nice to have
- The logo improved and turned into a separate vector file for future use would be a major plus.
- Some sort of leather looking fabric (grey, dark grey or some shade of blue) as a background to show more of an upholstery look if possible.
- -Use of all 13 provided photos if possible.
- -Logos of all the clients we have worked with.
Should not have
- Too Busy
- Too cluttered

```html
<!DOCTYPE html>
<html lang="en">
<head>
<meta charset="utf-8">
<title>Tarnwick Upholstery – Two-Page Flyer</title>
<link rel="stylesheet" href="https://fonts.googleapis.com/css2?family=Catamaran:wght@400;500;600&family=Hind:wght@400;500;600&display=swap">
<style>
  :root {
    --backdrop: #d6d6d6;
    --page-dark: #1d1e20;
    --page-mid: #2a2b2e;
    --blue: #1a8fd6;
    --white: #ffffff;
  }
  * { margin: 0; padding: 0; box-sizing: border-box; }
  html, body { width: 1200px; height: 1200px; overflow: hidden; }
  body { background: var(--backdrop); position: relative; font-family: "Catamaran", sans-serif; color: var(--white); }

  .flyer-page {
    position: absolute;
    width: 595px; height: 842px;
    transform-origin: 0 0;
    transform: scale(0.9);
    overflow: hidden;
    background: radial-gradient(circle at 40% 40%, var(--page-mid), var(--page-dark) 70%);
    box-shadow: 0 6px 18px rgba(0,0,0,0.18);
  }
  .flyer-page--front { left: 45px; top: 330px; }
  .flyer-page--back { left: 620px; top: 140px; }

  .page-art { position: absolute; inset: 0; width: 595px; height: 842px; }

  .brand { position: absolute; font-weight: 600; color: var(--white); line-height: 1; }
  .brand__name { display: block; font-size: 48px; letter-spacing: -0.5px; }
  .brand__sub { display: block; font-size: 13px; letter-spacing: 4.5px; margin-top: 2px; margin-left: 62px; }

  .front-brand { left: 46px; top: 42px; }
  .back-brand { left: 228px; top: 628px; }

  .mission-title { position: absolute; left: 45px; top: 634px; font-size: 27px; font-weight: 500; color: var(--blue); }
  .mission-text { position: absolute; left: 45px; top: 677px; width: 490px; font-size: 13px; line-height: 18px; font-weight: 500; }

  .page-title { position: absolute; left: 46px; top: 38px; font-size: 23px; font-weight: 500; }
  .page-lead { position: absolute; left: 43px; top: 85px; width: 360px; font-family: "Hind", sans-serif; font-size: 12.5px; line-height: 16px; font-weight: 500; }

  .page-body { position: absolute; left: 45px; top: 145px; width: 505px; font-family: "Hind", sans-serif; font-size: 10.4px; line-height: 13.5px; }
  .page-body__wrap {
    float: right; width: 300px; height: 220px;
    shape-outside: polygon(100px 0, 300px 0, 300px 220px, 290px 220px, 30px 40px);
  }
  .clients__title { font-family: "Catamaran", sans-serif; font-size: 12.5px; font-weight: 600; color: var(--blue); margin-top: 9px; letter-spacing: 0.5px; }
  .clients__list { margin-top: 1px; }

  .cta { position: absolute; left: 0; width: 615px; top: 390px; text-align: center; }
  .cta__heading { font-size: 19px; font-weight: 500; }
  .cta__email { font-size: 12.5px; font-weight: 500; margin-top: 2px; }

  .services { position: absolute; right: 44px; top: 474px; text-align: right; }
  .services__title { font-size: 19px; font-weight: 500; margin-bottom: 6px; }
  .services__list { list-style: none; font-size: 12.5px; font-weight: 500; line-height: 25px; }

  .contact-row { position: absolute; left: 0; width: 595px; }
  .front-contacts { top: 750px; }
  .back-contacts { top: 752px; }
  .contact-item { position: absolute; top: 0; transform: translateX(-50%); text-align: center; font-size: 10.8px; font-weight: 500; white-space: nowrap; }
  .contact-icon { display: block; width: 28px; height: 28px; margin: 0 auto 6px; }
</style>
</head>
<body>

<section class="flyer-page flyer-page--front">
  <svg class="page-art" viewBox="0 0 595 842">
    <defs>
      <linearGradient id="frontPhotoMain" x1="0" y1="0" x2="1" y2="1">
        <stop offset="0" stop-color="#3a332e"/>
        <stop offset="0.5" stop-color="#55504b"/>
        <stop offset="1" stop-color="#8a8078"/>
      </linearGradient>
      <linearGradient id="frontPhotoSide" x1="0" y1="0" x2="1" y2="1">
        <stop offset="0" stop-color="#6b4a30"/>
        <stop offset="1" stop-color="#2c2521"/>
      </linearGradient>
    </defs>
    <polygon role="img" aria-label="Restaurant interior with rows of grey upholstered booths and an open kitchen" points="595,0 595,680 247,488 0,342" fill="url(#frontPhotoMain)"/>
    <polygon role="img" aria-label="Lounge dining room with tufted leather banquettes under warm lights" points="0,342 247,488 0,628" fill="url(#frontPhotoSide)"/>
    <polygon points="0,235 85,285 0,338" fill="var(--blue)"/>
    <polyline points="595,0 0,340" fill="none" stroke="var(--blue)" stroke-width="6"/>
    <polyline points="0,342 247,488" fill="none" stroke="var(--blue)" stroke-width="5"/>
    <polyline points="0,628 247,488 595,680" fill="none" stroke="var(--blue)" stroke-width="6"/>
  </svg>

  <div class="brand front-brand">
    <span class="brand__name">Tarnwick</span>
    <span class="brand__sub">UPHOLSTERY</span>
  </div>

  <h2 class="mission-title">Our Mission</h2>
  <p class="mission-text">Our greatest desire is to know your needs, to communicate and to make your life easier by being a part of the solution.</p>

  <div class="contact-row front-contacts">
    <div class="contact-item" style="left:88px">
      <svg class="contact-icon" viewBox="0 0 28 28"><circle cx="14" cy="14" r="14" fill="var(--blue)"/><path d="M9.5 7.5l3 0 1 4-2 1.3a8 8 0 0 0 3.7 3.7l1.3-2 4 1v3c0 .8-.7 1.5-1.5 1.5A11 11 0 0 1 8 9c0-.8.7-1.5 1.5-1.5z" fill="var(--white)"/></svg>
      555-318-6472
    </div>
    <div class="contact-item" style="left:272px">
      <svg class="contact-icon" viewBox="0 0 28 28"><circle cx="14" cy="14" r="14" fill="var(--blue)"/><path d="M14 6a5.5 5.5 0 0 0-5.5 5.5c0 4 5.5 10.5 5.5 10.5s5.5-6.5 5.5-10.5A5.5 5.5 0 0 0 14 6z" fill="var(--white)"/><circle cx="14" cy="11.5" r="2.2" fill="var(--blue)"/></svg>
      4182 Mossvale Rd. Edmonton, AB. T9X 7K1
    </div>
    <div class="contact-item" style="left:475px">
      <svg class="contact-icon" viewBox="0 0 28 28"><circle cx="14" cy="14" r="14" fill="var(--blue)"/><g fill="none" stroke="var(--white)" stroke-width="1.4"><circle cx="14" cy="14" r="7"/><ellipse cx="14" cy="14" rx="3" ry="7"/><line x1="7" y1="14" x2="21" y2="14"/></g></svg>
      www.tarnwickupholstery.example
    </div>
  </div>
</section>

<section class="flyer-page flyer-page--back">
  <svg class="page-art" viewBox="0 0 595 842">
    <defs>
      <linearGradient id="backPhotoTop" x1="0" y1="0" x2="1" y2="1">
        <stop offset="0" stop-color="#3d5563"/>
        <stop offset="0.6" stop-color="#4a4440"/>
        <stop offset="1" stop-color="#6b5a4a"/>
      </linearGradient>
      <linearGradient id="backPhotoSide" x1="0" y1="0" x2="1" y2="1">
        <stop offset="0" stop-color="#8a7f72"/>
        <stop offset="1" stop-color="#5a3a26"/>
      </linearGradient>
    </defs>
    <polygon role="img" aria-label="Modern restaurant dining room with blue banquettes, tall windows and pendant lights" points="595,9 290,185 595,366" fill="url(#backPhotoTop)"/>
    <polygon role="img" aria-label="Diner wall of framed pictures above a long tufted brown leather booth" points="0,406 271,565 0,722" fill="url(#backPhotoSide)"/>
    <polygon points="595,626 490,686 595,746" fill="var(--blue)"/>
    <polyline points="595,7 290,185 595,367" fill="none" stroke="var(--blue)" stroke-width="6"/>
    <polyline points="0,406 271,565 0,722" fill="none" stroke="var(--blue)" stroke-width="6"/>
  </svg>

  <h1 class="page-title">Restaurant Reupholstery</h1>
  <p class="page-lead">Maintain your upholstery in the best possible condition until you need a major renovation!</p>

  <div class="page-body">
    <div class="page-body__wrap"></div>
    <p class="company-description">Tarnwick Upholstery has been serving North America for over 60 years. The company began as a family owned and operated business and has grown into a complete manufacturing facility. We can carry your vision straight through the manufacturing process, from initial drawings to finished product, including foam, fabric, framework, and associated millwork. Our 25,000 square foot facility has computer controlled cutters for both fabric and wood cutting capabilities. We have the capacity to take an original design and create products to meet your specifications, or adapt our standardized designs to fit your vision. We have a library of standard configurations that are customizable to meet almost any requirements.</p>
    <h2 class="clients__title">OUR CLIENTS</h2>
    <p class="clients__list">Halvern Arena &bull; The Silver Quarry Casino &bull; Dunmo &bull; Corvello Pizza &bull; PKLU &bull; Juniper Hall &bull; Faithful Teds &bull; Oar &amp; Lantern &bull; Brackley Crossing Mall &bull; Kesterfield Polytechnic &bull; Torvane &bull; And many more.</p>
  </div>

  <div class="cta">
    <p class="cta__heading">Send an e-mail to Tarnwick, outlining your requirements</p>
    <p class="cta__email">sales@tarnwickupholstery.example</p>
  </div>

  <div class="services">
    <h2 class="services__title">OUR SERVICES</h2>
    <ul class="services__list">
      <li>Specialty Services</li>
      <li>Transportation Reupholstery</li>
      <li>New Booths &amp; Furniture</li>
      <li>CNC Cutting Services</li>
    </ul>
  </div>

  <div class="brand back-brand">
    <span class="brand__name">Tarnwick</span>
    <span class="brand__sub">UPHOLSTERY</span>
  </div>

  <div class="contact-row back-contacts">
    <div class="contact-item" style="left:90px">
      <svg class="contact-icon" viewBox="0 0 28 28"><circle cx="14" cy="14" r="14" fill="var(--blue)"/><path d="M9.5 7.5l3 0 1 4-2 1.3a8 8 0 0 0 3.7 3.7l1.3-2 4 1v3c0 .8-.7 1.5-1.5 1.5A11 11 0 0 1 8 9c0-.8.7-1.5 1.5-1.5z" fill="var(--white)"/></svg>
      555-318-6472
    </div>
    <div class="contact-item" style="left:275px">
      <svg class="contact-icon" viewBox="0 0 28 28"><circle cx="14" cy="14" r="14" fill="var(--blue)"/><path d="M14 6a5.5 5.5 0 0 0-5.5 5.5c0 4 5.5 10.5 5.5 10.5s5.5-6.5 5.5-10.5A5.5 5.5 0 0 0 14 6z" fill="var(--white)"/><circle cx="14" cy="11.5" r="2.2" fill="var(--blue)"/></svg>
      4182 Mossvale Rd. Edmonton, AB. T9X 7K1
    </div>
    <div class="contact-item" style="left:477px">
      <svg class="contact-icon" viewBox="0 0 28 28"><circle cx="14" cy="14" r="14" fill="var(--blue)"/><g fill="none" stroke="var(--white)" stroke-width="1.4"><circle cx="14" cy="14" r="7"/><ellipse cx="14" cy="14" rx="3" ry="7"/><line x1="7" y1="14" x2="21" y2="14"/></g></svg>
      www.tarnwickupholstery.example
    </div>
  </div>
</section>

</body>
</html>
```